Create Vertical Dog Food Labels (3 inches x 5 inches) for PupKitchen

We need a packing Vertical label (3 inches x 5 inches) design for our line of Dog Food - Pup Kitchen at pupkitchenmeals.com (please review website). This design is for Custom Roll Labels. We have a logo already. Use our logo colors on label. What we need incorporated is a list of our ingredients:

50% Choice Beef
20% Pasture-raised Chicken
15% Brown Rice
15% Fresh Vegetables - Carrots, Kale, Zucchini
Herbal Health Boosters

We also need these lines at the bottom of the label:

Keeps in fridge for 4 days after thawing
Stores in freezer up to 6 months
Questions? email us at orders@meadowlanepantry.com

We have attached a sample of a competitor. The Kibble Crate.

Target Market(s)

Dog owners

Industry/Entity Type

Dog Food

Font styles to use
Sans Serif

Requirements
Must have
• Read project description above
Nice to have
• Our logo color incorporated
Should not have
• I want it simple.

```html
<!DOCTYPE html>
<html lang="en">
<head>
<meta charset="utf-8">
<title>PupKitchen – Dog Food Label</title>
<link rel="stylesheet" href="https://fonts.googleapis.com/css2?family=Montserrat:wght@800&family=Nunito:wght@600;800;900&family=Nunito+Sans:wght@600&display=swap">
<style>
  :root {
    --page-bg: #efefef;
    --label-white: #ffffff;
    --brand-green-dark: #1b6a36;
    --brand-green: #7dbb3f;
    --brand-green-light: #92c84a;
    --brand-orange: #ef5a2c;
    --ink: #222222;
    --rule: #cfcfcf;
  }
  * { margin: 0; padding: 0; box-sizing: border-box; }
  html, body {
    width: 1004px;
    height: 1200px;
    overflow: hidden;
    background: var(--page-bg);
  }
  .label {
    position: absolute;
    left: 173px;
    top: 52px;
    width: 658px;
    height: 1096px;
    background: var(--label-white);
    box-shadow: 0 2px 10px rgba(0,0,0,0.08);
    overflow: hidden;
    font-family: "Nunito", sans-serif;
  }

  /* Brand header */
  .brand {
    position: absolute;
    left: 0; top: 0;
    width: 100%; height: 207px;
    display: flex;
    align-items: center;
    justify-content: center;
    gap: 22px;
  }
  .brand-dot {
    width: 64px; height: 64px;
    border-radius: 50%;
    background: var(--brand-green);
  }
  .brand-name {
    font-family: "Nunito Sans", sans-serif;
    font-weight: 600;
    font-size: 42px;
    color: var(--brand-green-dark);
    letter-spacing: 0.5px;
  }

  /* Ingredient panel */
  .ingredients {
    position: absolute;
    left: 0; top: 207px;
    width: 100%; height: 433px;
    background: linear-gradient(135deg, var(--brand-green) 0%, var(--brand-green-light) 50%, var(--brand-green) 100%);
  }
  .ingredient {
    position: absolute;
    width: 230px;
    margin-left: -115px;
    text-align: center;
  }
  .ingredient-icon {
    display: block;
    margin: 0 auto;
  }
  .ingredient-percent {
    font-family: "Montserrat", sans-serif;
    font-weight: 800;
    font-size: 40px;
    line-height: 1;
    color: var(--brand-green-dark);
    margin-top: 8px;
  }
  .ingredient-name {
    font-weight: 900;
    font-size: 21px;
    line-height: 1.2;
    color: var(--label-white);
    margin-top: 6px;
  }
  .ing-beef    { left: 195px; top: 30px; }
  .ing-chicken { left: 430px; top: 30px; }
  .ing-rice    { left: 195px; top: 236px; }
  .ing-veg     { left: 430px; top: 236px; }

  .veg-arrow {
    position: absolute;
    left: 535px; top: 600px;
  }

  /* Vegetable band */
  .veg-band {
    position: absolute;
    left: 0; top: 640px;
    width: 100%; height: 75px;
    background: var(--brand-orange);
    display: flex;
    align-items: center;
    justify-content: center;
    padding-right: 60px;
  }
  .veg-item {
    display: flex;
    align-items: center;
    gap: 8px;
    font-weight: 900;
    font-size: 21px;
    color: var(--label-white);
    padding: 0 16px;
  }
  .veg-item + .veg-item { border-left: 2px solid rgba(0,0,0,0.18); }
  .veg-tick { flex: none; }

  /* Boosters heading */
  .boosters {
    position: absolute;
    left: 0; top: 745px;
    width: 100%;
    text-align: center;
    font-family: "Montserrat", sans-serif;
    font-weight: 800;
    font-size: 41px;
    line-height: 48px;
  }
  .boosters-top { color: var(--brand-green-dark); }
  .boosters-bottom { color: var(--brand-orange); }

  /* Storage notes */
  .storage {
    position: absolute;
    left: 105px; top: 862px;
    width: 448px;
    text-align: center;
    font-weight: 600;
    font-size: 19px;
    color: var(--ink);
  }
  .storage-line { line-height: 26px; }
  .storage-rule {
    height: 2px;
    background: var(--rule);
    margin: 10px 0 10px;
  }

  .contact {
    position: absolute;
    left: 90px; top: 965px;
    width: 478px; height: 64px;
    border-radius: 32px;
    background: var(--brand-green-dark);
    color: var(--label-white);
    display: flex;
    flex-direction: column;
    align-items: center;
    justify-content: center;
    font-weight: 800;
    font-size: 17px;
    line-height: 21px;
  }
</style>
</head>
<body>
  <main class="label">
    <header class="brand">
      <span class="brand-dot"></span>
      <span class="brand-name">PupKitchen</span>
    </header>

    <section class="ingredients">
      <div class="ingredient ing-beef">
        <svg class="ingredient-icon" width="92" height="92" viewBox="0 0 92 92" role="img" aria-label="Beef icon">
          <circle cx="46" cy="46" r="44" fill="none" stroke="var(--brand-green-dark)" stroke-width="2" stroke-dasharray="5 4"/>
          <circle cx="46" cy="46" r="38" fill="var(--brand-orange)"/>
        </svg>
        <div class="ingredient-percent">50%</div>
        <div class="ingredient-name">Choice Beef</div>
      </div>
      <div class="ingredient ing-chicken">
        <svg class="ingredient-icon" width="92" height="92" viewBox="0 0 92 92" role="img" aria-label="Chicken icon">
          <circle cx="46" cy="46" r="44" fill="none" stroke="var(--brand-green-dark)" stroke-width="2" stroke-dasharray="5 4"/>
          <circle cx="46" cy="46" r="38" fill="var(--brand-orange)"/>
        </svg>
        <div class="ingredient-percent">20%</div>
        <div class="ingredient-name">Pasture-raised<br>Chicken</div>
      </div>
      <div class="ingredient ing-rice">
        <svg class="ingredient-icon" width="92" height="92" viewBox="0 0 92 92" role="img" aria-label="Brown rice icon">
          <circle cx="46" cy="46" r="44" fill="none" stroke="var(--brand-green-dark)" stroke-width="2" stroke-dasharray="5 4"/>
          <circle cx="46" cy="46" r="38" fill="var(--brand-orange)"/>
        </svg>
        <div class="ingredient-percent">15%</div>
        <div class="ingredient-name">Brown Rice</div>
      </div>
      <div class="ingredient ing-veg">
        <svg class="ingredient-icon" width="92" height="92" viewBox="0 0 92 92" role="img" aria-label="Vegetables icon">
          <circle cx="46" cy="46" r="44" fill="none" stroke="var(--brand-green-dark)" stroke-width="2" stroke-dasharray="5 4"/>
          <circle cx="46" cy="46" r="38" fill="var(--brand-orange)"/>
        </svg>
        <div class="ingredient-percent">15%</div>
        <div class="ingredient-name">Fresh Vegetables</div>
      </div>
    </section>

    <section class="veg-band">
      <span class="veg-item">
        <svg class="veg-tick" width="20" height="20" viewBox="0 0 20 20"><circle cx="10" cy="10" r="10" fill="var(--brand-green-dark)"/><path d="M5.5 10.3l3 3 6-6.2" fill="none" stroke="#fff" stroke-width="2.2" stroke-linecap="round" stroke-linejoin="round"/></svg>
        Carrots
      </span>
      <span class="veg-item">
        <svg class="veg-tick" width="20" height="20" viewBox="0 0 20 20"><circle cx="10" cy="10" r="10" fill="var(--brand-green-dark)"/><path d="M5.5 10.3l3 3 6-6.2" fill="none" stroke="#fff" stroke-width="2.2" stroke-linecap="round" stroke-linejoin="round"/></svg>
        Kale
      </span>
      <span class="veg-item">
        <svg class="veg-tick" width="20" height="20" viewBox="0 0 20 20"><circle cx="10" cy="10" r="10" fill="var(--brand-green-dark)"/><path d="M5.5 10.3l3 3 6-6.2" fill="none" stroke="#fff" stroke-width="2.2" stroke-linecap="round" stroke-linejoin="round"/></svg>
        Zucchini
      </span>
    </section>

    <svg class="veg-arrow" width="50" height="90" viewBox="0 0 50 90" aria-hidden="true">
      <path d="M6 4 C 22 14, 30 28, 20 36 C 10 44, 8 30, 20 32 C 36 36, 30 66, 14 76" fill="none" stroke="#1d1d1d" stroke-width="2" stroke-dasharray="4 3"/>
      <path d="M20 70 L12 77 L21 81" fill="none" stroke="#1d1d1d" stroke-width="2" stroke-linecap="round" stroke-linejoin="round"/>
    </svg>

    <h2 class="boosters">
      <span class="boosters-top">HERBAL HEALTH</span><br>
      <span class="boosters-bottom">BOOSTERS</span>
    </h2>

    <section class="storage">
      <p class="storage-line">Keeps in fridge for 4 days after thawing</p>
      <div class="storage-rule"></div>
      <p class="storage-line">Stores in freezer up to 6 months</p>
    </section>

    <div class="contact">
      <span>Questions? email us at</span>
      <span>orders@meadowlanepantry.com</span>
    </div>
  </main>
</body>
</html>
```